23rd Annual Harrowgate Lantern Film Festival Poster

Design an eye catchy, stylish poster for our 23rd film festival. Be different not just a poster with a film reel. Think outside of the box with a design that will attract peoples attention. Colorful (you choose the colors). Make it fun and creative, like the film festival. Show your talents in the design. Be sure it is new and stylish. Dates are August 21 - 29, 2020. Poster size will be 27 inches by 40 inches

Target Market(s)

Upper Middle class - movie lovers

Font styles to use
Sans Serif

Colors
33a6d7

Requirements
Must have
• NO CLIP ART - be original !
Nice to have
• abstract - think outside the box
Should not have
• CLIP ART

```html
<!DOCTYPE html>
<html lang="en">
<head>
<meta charset="utf-8">
<title>23rd Harrowgate Lantern Film Festival Poster</title>
<link rel="stylesheet" href="https://fonts.googleapis.com/css2?family=Poppins:wght@600&family=Amatic+SC:wght@700&display=swap">
<style>
  :root {
    --page-bg: #ecebef;
    --violet-light: #7a62b0;
    --violet-deep: #452a88;
    --violet-shade: #3d2a80;
    --orchid: #8a4fa3;
    --panel-cream: #efede8;
    --panel-border: #4a7cc0;
    --accent-green: #8cc63f;
    --accent-pink: #e0267c;
    --ink: #1f1b24;
    --line-white: rgba(255,255,255,0.75);
    --text-white: #ffffff;
  }
  * { margin: 0; padding: 0; box-sizing: border-box; }
  html, body { width: 1200px; height: 1200px; overflow: hidden; background: var(--page-bg); }
  .canvas { position: relative; width: 1200px; height: 1200px; }
  .poster {
    position: absolute; left: 235px; top: 40px; width: 730px; height: 1120px;
    overflow: hidden; box-shadow: 0 6px 24px rgba(40,20,80,0.18);
  }
  .poster-art { position: absolute; inset: 0; }

  .festival-mark {
    position: absolute; left: 0; right: 0; top: 72px;
    display: flex; flex-direction: column; align-items: center;
  }
  .festival-mark__dot {
    width: 70px; height: 70px; border-radius: 50%; background: var(--accent-green);
    margin-bottom: 14px;
  }
  .festival-mark__name {
    font-family: 'Poppins', sans-serif; font-weight: 600; font-size: 86px;
    line-height: 1; letter-spacing: 6px; color: var(--text-white);
  }
  .festival-mark__full {
    margin-top: 10px;
    font-family: 'Poppins', sans-serif; font-weight: 600; font-size: 15px;
    line-height: 1; letter-spacing: 0.5px; text-transform: uppercase; color: var(--text-white);
  }

  .title-panel__text { position: absolute; left: 79px; top: 351px; width: 453px; height: 246px; }
  .title-panel__edition {
    position: absolute; left: 18px; top: 14px;
    font-family: 'Amatic SC', sans-serif; font-weight: 700; font-size: 64px;
    line-height: 1; color: var(--ink);
  }
  .title-panel__edition sup { font-size: 30px; vertical-align: 28px; margin-left: 2px; }
  .title-panel__name {
    position: absolute; left: 0; right: 0; top: 112px; text-align: center;
    font-family: 'Poppins', sans-serif; font-weight: 600; font-size: 33px;
    line-height: 1; letter-spacing: 1px; text-transform: uppercase; color: var(--accent-pink);
  }
  .title-panel__sub {
    position: absolute; left: 0; right: 0; top: 166px; text-align: center;
    font-family: 'Amatic SC', sans-serif; font-weight: 700; font-size: 46px;
    line-height: 1; letter-spacing: 4px; color: var(--ink);
  }

  .festival-dates {
    position: absolute; left: 208px; top: 632px; width: 360px;
    font-family: 'Amatic SC', sans-serif; font-weight: 700; font-size: 78px;
    letter-spacing: 6px; color: var(--text-white);
  }
  .festival-dates span { display: block; height: 64px; line-height: 64px; }
  .festival-dates .year { letter-spacing: 16px; }
</style>
</head>
<body>
<div class="canvas">
  <main class="poster">
    <svg class="poster-art" width="730" height="1120" viewBox="0 0 730 1120" aria-hidden="true">
      <defs>
        <linearGradient id="poster-bg" x1="0" y1="0" x2="1" y2="1">
          <stop offset="0" stop-color="#7a62b0"/>
          <stop offset="0.45" stop-color="#452a88"/>
          <stop offset="1" stop-color="#8a4fa3"/>
        </linearGradient>
        <linearGradient id="wave-bottom" x1="0" y1="0" x2="1" y2="0">
          <stop offset="0" stop-color="#5a3f9f"/>
          <stop offset="1" stop-color="#8550a5"/>
        </linearGradient>
      </defs>
      <rect class="backdrop" width="730" height="1120" fill="url(#poster-bg)"/>
      <path class="blob-top" d="M110 300 C150 160 300 70 470 60 C580 52 650 20 730 0 L730 380 C660 330 560 250 440 260 C300 270 170 360 110 300 Z" fill="#ffffff" opacity="0.06"/>
      <circle class="orb" cx="486" cy="670" r="263" fill="#3d2a80" opacity="0.55"/>
      <path class="wave-bottom" d="M0 1020 C40 880 160 820 300 830 C430 840 520 760 730 690 L730 1120 L0 1120 Z" fill="url(#wave-bottom)" opacity="0.55"/>
      <g class="hairlines" stroke="rgba(255,255,255,0.75)" stroke-width="1.2">
        <line x1="26" y1="4" x2="26" y2="152"/>
        <line x1="35" y1="4" x2="35" y2="152"/>
        <line x1="43" y1="4" x2="43" y2="152"/>
        <line x1="493" y1="55" x2="650" y2="55"/>
        <line x1="525" y1="60" x2="650" y2="60"/>
        <line x1="552" y1="174" x2="552" y2="399"/>
        <line x1="568" y1="188" x2="568" y2="399"/>
        <line x1="0" y1="810" x2="62" y2="810"/>
        <line x1="18" y1="814" x2="76" y2="814"/>
        <line x1="660" y1="920" x2="660" y2="1120"/>
        <line x1="668" y1="930" x2="668" y2="1120"/>
        <line x1="678" y1="945" x2="678" y2="1120"/>
      </g>
      <path class="title-panel" d="M79 351 H219 V446 H532 V597 H79 Z"
        fill="#efede8" stroke="#4a7cc0" stroke-width="4"/>
    </svg>

    <header class="festival-mark">
      <span class="festival-mark__dot"></span>
      <span class="festival-mark__name">HLFF</span>
      <span class="festival-mark__full">Harrowgate Lantern Film Festival</span>
    </header>

    <div class="title-panel__text">
      <p class="title-panel__edition">23<sup>RD</sup></p>
      <h1 class="title-panel__name">Harrowgate Lantern</h1>
      <p class="title-panel__sub">FILM FESTIVAL</p>
    </div>

    <p class="festival-dates">
      <span>21- August</span>
      <span class="year">29 2020</span>
    </p>
  </main>
</div>
</body>
</html>
```